Top of the line business card design needed for real estate brokerage

We currently have a business card with our logo but would like to have a revised version. We would love for you to implement your own design that will catch anyone's attention. The theme colors should be black, royal blue, gray/silver, and white.The contact information should be the same as the info on our current business card (picture attached). In the design that we pick, we will need to be able to edit the text so that we can customize the text content for each of our agents. Same goes for the professional picture. There should be an area on the card that each agent can have their professional portrait attached. Please include a version without the picture option as well for agents that do not wish to have a professional picture attached.

```html
<!DOCTYPE html>
<html lang="en">
<head>
<meta charset="utf-8">
<title>Clear Harbor Realty – Business Card</title>
<link href="https://fonts.googleapis.com/css2?family=PT+Sans:wght@400;700&display=swap" rel="stylesheet">
<style>
  :root {
    --stage: #141414;
    --card-light: #f3f3f3;
    --card-blue: #0052a5;
    --royal: #0a4aa0;
    --ink: #1c1c1c;
    --white: #ffffff;
  }
  * { margin: 0; padding: 0; box-sizing: border-box; }
  html, body {
    width: 1200px; height: 900px; overflow: hidden;
    background: var(--stage);
    font-family: "PT Sans", "Myriad Pro", sans-serif;
  }
  .canvas { position: relative; width: 1200px; height: 900px; }
  .card {
    position: absolute; top: 184px; height: 490px;
    border-radius: 12px;
    box-shadow: 0 2px 6px rgba(0,0,0,.45);
    text-align: center;
  }
  .card--front { left: 299px; width: 301px; background: var(--card-light); color: var(--ink); }
  .card--back  { left: 645px; width: 305px; background: var(--card-blue); color: var(--white); }

  .brand {
    position: absolute; left: 0; right: 0;
    font-weight: 700; font-size: 30px; line-height: 34px;
  }
  .card--front .brand { top: 305px; color: var(--royal); top: 118px; }
  .card--back .brand { top: 150px; color: var(--white); }
  .brand__mark {
    display: block; width: 14px; height: 14px; margin: 0 auto 12px;
  }
  .card--front .brand__mark { background: var(--royal); }
  .card--back .brand__mark { background: var(--white); }

  .agent { position: absolute; left: 0; right: 0; top: 255px; }
  .agent__name {
    color: var(--royal); font-weight: 700; font-size: 17px;
    letter-spacing: .3px; text-transform: uppercase; line-height: 22px;
  }
  .agent__title { font-size: 13px; line-height: 18px; }
  .agent__address { margin-top: 12px; font-size: 13.5px; line-height: 18px; }
  .agent__contact { margin-top: 12px; font-size: 13.5px; line-height: 17.6px; }

  .services {
    position: absolute; left: 0; right: 0; top: 317px;
    list-style: none; font-size: 17px; line-height: 24.2px;
  }
</style>
</head>
<body>
<main class="canvas">
  <section class="card card--front" aria-label="Card front">
    <div class="brand"><span class="brand__mark"></span>Clear Harbor<br>Realty</div>
    <div class="agent">
      <p class="agent__name">Marcel Tavenor</p>
      <p class="agent__title">Broker</p>
      <p class="agent__address">2400 Lakeview Pkwy, Suite 310<br>Palm Grove, FL 33410</p>
      <p class="agent__contact">
        555-210-4831<br>
        555-210-7962<br>
        555-340-1187<br>
        marcel@clearharborrealty.com<br>
        www.clearharborrealty.com
      </p>
    </div>
  </section>

  <section class="card card--back" aria-label="Card back">
    <div class="brand"><span class="brand__mark"></span>Clear Harbor<br>Realty</div>
    <ul class="services">
      <li>Residential Real Estate</li>
      <li>Commercial Real Estate</li>
      <li>Property Management</li>
      <li>Investments</li>
    </ul>
  </section>
</main>
</body>
</html>
```